Etiketten - WINE LABEL for a natural wine
Zielgruppe
The family winery Lorenz Falkner stands for first-class wines from the Traisental and is considered to be one of the flagship wineries of the wine country Austria. The region's leading winery produces distinctive wines full of character on unique limestone conglomerate soils, with clear-as-a-bell stylistics and minerality accentuated by the terroir. Uncompromising work in the vineyard and cellar in favour of the highest quality is the highest premise of the Lorenz Falkner winery. In terms of a holistic understanding of nature, the vineyards are cultivated according to organic guidelines, and the entire winery is also certified according to the Grüne Rebe Standard standard. In addition to numerous national and international awards, Lorenz Falkner was named 'Vinoria Winemaker of the Year', the Oscar of the Austrian wine industry, at a young age. The wines of the Lorenz Falkner winery can be found in more than 35 nations worldwide, making the winery one of the most successful exporters of Austrian wines in the premium segment.
Our target group for this project are Natural Wine lovers. Natural wines are wines which don´t contain any additives, they are unfiltered(cloudy). Natural Wines have gained a lot of market share in the last years, the target group are people who like natural wine.
Aufgabenstellung
We are looking for a front label for our wine bottle. The bottle conists from white glas, the wine has an yellow-orange colour. The wine is cloudy. (picture of the bottle without labels in graphic atteched)
The brand name for this wine is WELLENSPIEL.
The maximum label dimensions can be 100 mm in height and 120 mm in width. Any size of the label within these parameters is possible.
The label can go in two directions.
Either a clear, reduced, minimalist design or a bolder, attention-grabbing more edgy design.
In both variants, the brand name WELLENSPIEL must be very clearly recognizable, as this creates the brand value of the product.

```html
<!DOCTYPE html>
<html lang="en">
<head>
<meta charset="utf-8">
<title>Wellenspiel – Natural Wine Label</title>
<link rel="stylesheet" href="https://fonts.googleapis.com/css2?family=Rubik+Mono+One&family=Red+Hat+Display:wght@400&display=swap">
<style>
  :root {
    --label-plum: #63184a;
    --label-white: #ffffff;
  }
  html, body {
    margin: 0;
    padding: 0;
    width: 1200px;
    height: 1001px;
    overflow: hidden;
    background: var(--label-plum);
  }
  .wine-label {
    position: relative;
    width: 1200px;
    height: 1001px;
    background: var(--label-plum);
    color: var(--label-white);
  }
  .brand-wordmark {
    position: absolute;
    left: 0;
    top: 0;
    width: 1200px;
    height: 1001px;
  }
  .brand-wordmark text {
    font-family: "Rubik Mono One", "Arial Black", sans-serif;
    font-size: 274px;
    fill: var(--label-white);
  }
  .wine-style {
    position: absolute;
    left: 852px;
    top: 606px;
    margin: 0;
    font-family: "Red Hat Display", "Helvetica Neue", sans-serif;
    font-weight: 400;
    font-size: 50px;
    line-height: 58px;
    letter-spacing: 4px;
    text-transform: uppercase;
  }
  .origin {
    position: absolute;
    left: 851px;
    top: 896px;
    display: flex;
    align-items: center;
    gap: 26px;
    font-family: "Red Hat Display", "Helvetica Neue", sans-serif;
    font-weight: 400;
    font-size: 29px;
    letter-spacing: 4px;
    text-transform: uppercase;
  }
  .origin-dot {
    width: 20px;
    height: 20px;
    display: block;
    background: var(--label-white);
  }
</style>
</head>
<body>
  <main class="wine-label">
    <svg class="brand-wordmark" viewBox="0 0 1200 1001" role="img" aria-label="WELLENSPIEL">
      <text x="78" y="288" textLength="702" lengthAdjust="spacingAndGlyphs">WEL</text>
      <text x="78" y="504" textLength="702" lengthAdjust="spacingAndGlyphs">LEN</text>
      <text x="78" y="720" textLength="702" lengthAdjust="spacingAndGlyphs">SPI</text>
      <text x="78" y="936" textLength="702" lengthAdjust="spacingAndGlyphs">EL</text>
    </svg>

    <p class="wine-style">Natural<br>Wine</p>

    <div class="origin">
      <span class="origin-dot" aria-hidden="true"></span>
      <span class="origin-name">Austria</span>
    </div>
  </main>
</body>
</html>
```